Real Estate Listing Signs for standard Yard arms

I need real estate listing signs done, for the standard sized sign to be hung beneath a white yard arm. To match existing logo. Information to be included:
-Logo
-Business name
-Phone number
-Marden Fosk Tundra Circle & Marden Fosk Realty logos (smaller print)

Colors to be Red and anywhere in the gray scale between black and white, or a combination of those.

Target Market(s)

Drive by visuals

Industry/Entity Type

Real Estate Agent

Colors

Designer to choose only greyscale colors for use in the design.

Requirements
Must have
• My Logo and business name in same/similar font to whats provided, the MF tundra circle logo (small on bottom or corner somewhere), My phone number, and a decent amount of red coloration on the sign.

```html
<!DOCTYPE html>
<html lang="en">
<head>
<meta charset="utf-8">
<title>Brenvik Realty – Yard Sign</title>
<link rel="stylesheet" href="https://fonts.googleapis.com/css2?family=Montserrat:wght@800&family=Lato:wght@400;700&display=swap">
<style>
  :root {
    --backdrop: #e6e6e6;
    --sign-white: #ffffff;
    --sign-black: #050505;
    --brand-red: #ee3a33;
    --text-black: #0a0a0a;
    --text-white: #ffffff;
  }
  html, body {
    margin: 0;
    padding: 0;
    width: 1023px;
    height: 1200px;
    overflow: hidden;
    background: var(--backdrop);
  }
  .yard-sign {
    position: absolute;
    left: 71px;
    top: 22px;
    width: 880px;
    height: 1155px;
    background: var(--sign-black);
    box-shadow: 0 6px 18px rgba(0,0,0,0.18);
    overflow: hidden;
  }
  .sign-top {
    position: absolute;
    left: 0; top: 0;
    width: 100%;
    height: 692px;
    background: var(--sign-white);
  }
  .brand-mark {
    position: absolute;
    left: 355px;
    top: 200px;
    width: 170px;
    height: 170px;
    background: var(--brand-red);
  }
  .business-name {
    position: absolute;
    left: 0; right: 0;
    top: 462px;
    margin: 0;
    text-align: center;
    font-family: "Montserrat", sans-serif;
    font-weight: 800;
    font-size: 72px;
    letter-spacing: 1px;
    color: var(--text-black);
  }
  .divider {
    position: absolute;
    left: 0;
    top: 684px;
    width: 100%;
    height: 60px;
  }
  .phone {
    position: absolute;
    left: 0; right: 0;
    top: 790px;
    margin: 0;
    text-align: center;
    font-family: "Lato", sans-serif;
    font-weight: 400;
    font-size: 88px;
    letter-spacing: 1px;
    color: var(--brand-red);
  }
  .brokerage {
    position: absolute;
    left: 0; right: 0;
    top: 930px;
    text-align: center;
    font-family: "Lato", sans-serif;
    color: var(--text-white);
  }
  .brokerage-name {
    display: block;
    font-weight: 700;
    font-size: 52px;
    line-height: 1.1;
    letter-spacing: -0.5px;
  }
  .brokerage-sub {
    display: block;
    font-weight: 400;
    font-size: 26px;
    letter-spacing: 0.5px;
    margin-top: 4px;
  }
</style>
</head>
<body>
  <div class="yard-sign">
    <div class="sign-top">
      <div class="brand-mark"></div>
      <h1 class="business-name">BRENVIK REALTY</h1>
    </div>

    <svg class="divider" viewBox="0 0 880 60" aria-hidden="true">
      <rect x="0" y="0" width="880" height="16" fill="var(--brand-red)"/>
      <polygon points="440,-22 482,20 440,62 398,20" fill="var(--sign-white)"/>
      <polygon points="440,-6 466,20 440,46 414,20" fill="var(--sign-black)"/>
    </svg>

    <p class="phone">907-555-0148</p>

    <div class="brokerage">
      <span class="brokerage-name">MF TUNDRA CIRCLE</span>
      <span class="brokerage-sub">MARDEN FOSK REALTY</span>
    </div>
  </div>
</body>
</html>
```